Business Card and Logo tweak for a Language Boarding School

we are a boadring langauge school for under 18 international student.
We call ourselves " HCSC" - Harwick Crossway Study Centre
We are one of the TQ "tidewater quarters" Melbourne campus for TQ high school preparation program.

our address is 14 Orrin Lane Brighton 3187
Ph: 03 95550142
Email: info@myhcsc-example.com
Website: www.myhcsc-example.com

We have our HCSC logo, but not very satisfied. May be you can tweak it furhter with the fond or formations.

Basically the business card list all relevant info on one side and list all our programs on the other side.

The program we have:
ELICOS with Boarding for U18 Students
HSP-High School Preparation Program
PSP- Primary School Preparation Program
Junior Holiday Program & Study Tours
After School Tutoring
Student Wellbeing and Counselling

```html
<!DOCTYPE html>
<html lang="en">
<head>
<meta charset="utf-8">
<title>HCSC Business Card</title>
<link href="https://fonts.googleapis.com/css2?family=Arimo:wght@400;700&display=swap" rel="stylesheet">
<style>
  :root {
    --backdrop: #e9e9e9;
    --card: #2f2f2f;
    --card-back: #2b2b2b;
    --ink: #ffffff;
    --accent: #e5134d;
    --emboss: #5a5a5a;
    --rule: #d9d9d9;
  }
  * { margin: 0; padding: 0; box-sizing: border-box; }
  html, body {
    width: 1200px; height: 802px; overflow: hidden;
    background: var(--backdrop);
    font-family: "Arimo", Arial, sans-serif;
  }
  .stage {
    position: relative; width: 1200px; height: 802px;
    display: flex; align-items: center; justify-content: center; gap: 50px;
  }
  .card {
    position: relative; width: 540px; height: 310px;
    background: var(--card); color: var(--ink);
    box-shadow: 0 6px 18px rgba(0,0,0,0.18);
  }
  .card--back { background: var(--card-back); }

  .brand {
    position: absolute; left: 190px; top: 62px;
    display: flex; align-items: center; gap: 12px;
    font-weight: 400; font-size: 16px; line-height: 20px;
    color: var(--ink);
  }
  .brand__mark {
    width: 34px; height: 34px; border: 2px solid var(--ink); flex: none;
  }
  .divider {
    position: absolute; left: 200px; top: 160px; width: 310px; height: 1px;
    background: var(--rule);
  }
  .address {
    position: absolute; right: 30px; top: 180px; text-align: right;
    font-style: normal; font-size: 15px; line-height: 20px;
  }
  .person { position: absolute; left: 34px; top: 150px; }
  .person__name {
    color: var(--accent); font-weight: 700; font-size: 21px;
    text-transform: uppercase; letter-spacing: 0.3px;
  }
  .person__role { font-size: 15px; margin-top: 4px; }
  .person__rule { width: 150px; height: 1px; background: var(--rule); margin-top: 10px; }
  .contacts { list-style: none; margin-top: 10px; font-size: 15px; }
  .contacts li { display: flex; align-items: center; gap: 9px; height: 22px; }
  .contacts svg { width: 14px; height: 14px; flex: none; }

  .programs {
    position: absolute; left: 60px; top: 50px; right: 40px;
    color: var(--emboss);
  }
  .programs__title { font-size: 18px; font-weight: 700; margin-bottom: 18px; }
  .programs__list { list-style: none; font-size: 15px; line-height: 糖; }
  .programs__list li { height: 29px; display: flex; align-items: center; gap: 10px; }
  .programs__list li::before {
    content: ""; width: 6px; height: 6px; background: var(--emboss); flex: none;
  }
</style>
</head>
<body>
<main class="stage">
  <section class="card card--front">
    <div class="brand">
      <span class="brand__mark"></span>
      <span class="brand__name">Harwick Crossway<br>Study Centre</span>
    </div>
    <div class="divider"></div>
    <address class="address">14 Orrin Lane<br>Brighton 3187</address>
    <div class="person">
      <div class="person__name">Daniel Rowe</div>
      <div class="person__role">Manager</div>
      <div class="person__rule"></div>
      <ul class="contacts">
        <li>
          <svg viewBox="0 0 16 16" aria-hidden="true"><path fill="var(--accent)" d="M3.5 1.5l2.5 0 1 3.5-1.6 1.2c.8 1.8 2.2 3.2 4 4l1.2-1.6 3.4 1V13c0 .8-.7 1.5-1.5 1.5C6.6 14.5 1.5 9.4 1.5 3c0-.8.7-1.5 2-1.5z"/></svg>
          03 95550142
        </li>
        <li>
          <svg viewBox="0 0 16 16" aria-hidden="true"><rect x="1" y="3" width="14" height="10" rx="1" fill="var(--accent)"/><path d="M1.5 3.8L8 9l6.5-5.2" stroke="var(--card)" stroke-width="1.4" fill="none"/></svg>
          info@myhcsc-example.com
        </li>
        <li>
          <svg viewBox="0 0 16 16" aria-hidden="true"><circle cx="8" cy="8" r="7" fill="var(--accent)"/><path d="M1.5 8h13M8 1.2c-2.5 2.4-2.5 11.2 0 13.6M8 1.2c2.5 2.4 2.5 11.2 0 13.6" stroke="var(--card)" stroke-width="1.1" fill="none"/></svg>
          www.myhcsc-example.com
        </li>
      </ul>
    </div>
  </section>

  <section class="card card--back">
    <div class="programs">
      <div class="programs__title">Our Programs</div>
      <ul class="programs__list">
        <li>ELICOS with Boarding for U18 Students</li>
        <li>HSP - High School Preparation Program</li>
        <li>PSP - Primary School Preparation Program</li>
        <li>Junior Holiday Program &amp; Study Tours</li>
        <li>After School Tutoring</li>
        <li>Student Wellbeing and Counselling</li>
      </ul>
    </div>
  </section>
</main>
</body>
</html>
```